Business Card Design Project

Hi I am after a business card double sided 1 side to have the attached PDF on front on the back:

Trent Malloway - Managing Director
Mobile: 0413 268 471
email: trent@vrixo.com.au
web: www.vrixo.com.au

Industry/Entity Type

Business

Font styles to use
Sans Serif

Requirements
Must have
• I want a classy looking card
Nice to have
• I like lime green and black and white

```html
<!DOCTYPE html>
<html lang="en">
<head>
<meta charset="utf-8">
<title>Vrixo Lawns and Gardens – Business Card</title>
<link href="https://fonts.googleapis.com/css2?family=Lato:wght@300;400;700&display=swap" rel="stylesheet">
<style>
  :root {
    --backdrop: #8c8c8c;
    --card-black: #0b0b0b;
    --lime: #8cc43c;
    --lime-deep: #7ab52f;
    --brand-green: #3aa84a;
    --white: #ffffff;
    --ink: #111111;
    --contact: #e9f5d8;
  }
  * { box-sizing: border-box; margin: 0; padding: 0; }
  html, body {
    width: 1200px; height: 717px; overflow: hidden;
    background: var(--backdrop);
    font-family: "Lato", Arial, sans-serif;
  }
  .canvas {
    position: relative; width: 1200px; height: 717px;
    display: flex; align-items: center; justify-content: center; gap: 60px;
  }
  .card {
    position: relative; width: 520px; height: 318px; overflow: hidden;
    box-shadow: 0 6px 18px rgba(0,0,0,.3);
  }
  /* Front */
  .card--front {
    background: var(--card-black);
    display: flex; align-items: center; justify-content: center;
  }
  .brand { display: flex; align-items: center; gap: 16px; }
  .brand__square { width: 34px; height: 34px; background: var(--brand-green); }
  .brand__name {
    color: var(--white); font-weight: 300; font-size: 27px; letter-spacing: .5px;
  }
  /* Back */
  .card--back {
    background: linear-gradient(160deg, var(--lime) 0%, var(--lime-deep) 100%);
  }
  .curl { position: absolute; inset: 0; width: 520px; height: 318px; }
  .person { position: absolute; left: 48px; top: 52px; }
  .person__name {
    color: var(--white); font-weight: 300; font-size: 25px; letter-spacing: .3px;
  }
  .person__role {
    color: var(--ink); font-weight: 700; font-size: 11px; margin-top: 1px; margin-left: 2px;
  }
  .contacts { position: absolute; left: 46px; top: 168px; list-style: none; }
  .contacts__item {
    display: flex; align-items: center; gap: 10px;
    color: var(--contact); font-weight: 300; font-size: 13px; height: 22px;
  }
  .contacts__icon { width: 11px; height: 11px; fill: var(--ink); flex: none; }
</style>
</head>
<body>
<main class="canvas">
  <section class="card card--front" aria-label="Card front">
    <div class="brand">
      <span class="brand__square"></span>
      <span class="brand__name">Vrixo Lawns and Gardens</span>
    </div>
  </section>

  <section class="card card--back" aria-label="Card back">
    <svg class="curl" viewBox="0 0 520 318" aria-hidden="true">
      <defs>
        <linearGradient id="flap" x1="0" y1="0" x2="1" y2="1">
          <stop offset="0" stop-color="#f4f9e6"/>
          <stop offset=".35" stop-color="#c9e39a"/>
          <stop offset=".75" stop-color="#8dbf45"/>
          <stop offset="1" stop-color="#5e9226"/>
        </linearGradient>
      </defs>
      <path d="M340 0 L520 0 L520 258 C480 248 440 255 398 272 C420 200 400 90 340 0 Z" fill="#0b0b0b"/>
      <path d="M340 0 C400 90 420 200 398 272 C430 235 455 210 470 190 C430 150 395 70 340 0 Z" fill="url(#flap)"/>
    </svg>

    <div class="person">
      <p class="person__name">Trent Malloway</p>
      <p class="person__role">managing director</p>
    </div>

    <ul class="contacts">
      <li class="contacts__item">
        <svg class="contacts__icon" viewBox="0 0 12 12"><rect x="3" y="0" width="6" height="12" rx="1"/><rect x="4" y="1.5" width="4" height="6" fill="#8cc43c"/></svg>
        0413 268 471
      </li>
      <li class="contacts__item">
        <svg class="contacts__icon" viewBox="0 0 12 12"><rect x="0" y="2.5" width="12" height="7.5" rx="1"/><path d="M0.5 3 L6 7 L11.5 3" stroke="#8cc43c" stroke-width="1" fill="none"/></svg>
        trent@vrixo.com.au
      </li>
      <li class="contacts__item">
        <svg class="contacts__icon" viewBox="0 0 12 12"><circle cx="6" cy="6" r="5.5"/><path d="M0.5 6 H11.5 M6 0.5 V11.5 M6 0.5 C3 3 3 9 6 11.5 M6 0.5 C9 3 9 9 6 11.5" stroke="#8cc43c" stroke-width=".8" fill="none"/></svg>
        www.vrixo.com.au
      </li>
    </ul>
  </section>
</main>
</body>
</html>
```